Velvet Pressings Techno Label Business Card

I'm looking for a very clean business card for my Velvet Pressings music label. The label focusses on techno music. The card should include:

• my name : Bram Quintel as "Founder & CEO"
• email address: bram@velvet-pressings.example
• web: www.velvet-pressings.example
• facebook logo + /velvetpress
• twitter logo + /velvetpress
• soundcloud logo + /velvetpressings

Feel free to include your ideas! I'm looking forward to discuss about it.

Bram

Industry/Entity Type

Business

Contact Information for Business Card

I don't like glossy cards. Prefer matt.

Requirements
Nice to have
• Maybe on one side the complete logo, other side just the icon.
Should not have
• Flashy stuff. Must be clean and business like style.

```html
<!DOCTYPE html>
<html lang="en">
<head>
<meta charset="utf-8">
<title>Velvet Pressings — Business Card</title>
<link rel="stylesheet" href="https://fonts.googleapis.com/css2?family=Lato:wght@400;700;900&display=swap">
<style>
  :root {
    --backdrop: #e9e6e1;
    --card: #1e1e1f;
    --card-edge: #141415;
    --orange: #f0891c;
    --grey: #8b8b8b;
    --text-light: #a4a4a4;
  }
  * { box-sizing: border-box; margin: 0; padding: 0; }
  html, body { width: 1200px; height: 1023px; overflow: hidden; }
  body {
    background: var(--backdrop);
    font-family: "Lato", Arial, sans-serif;
    position: relative;
  }
  .card {
    position: absolute;
    top: 214px;
    width: 340px;
    height: 595px;
    background: var(--card);
    border-radius: 3px;
    box-shadow: 0 2px 0 var(--card-edge), 0 10px 26px rgba(0,0,0,.22);
  }
  .card--front { left: 220px; }
  .card--back { left: 640px; }

  /* front */
  .front-inner {
    display: flex;
    flex-direction: column;
    align-items: center;
    padding-top: 52px;
    text-align: center;
  }
  .brand-mark {
    display: flex;
    align-items: center;
    gap: 10px;
    color: var(--orange);
    font-weight: 700;
    font-size: 15px;
    letter-spacing: .5px;
  }
  .brand-dot {
    width: 22px; height: 22px;
    border: 4px solid var(--orange);
    border-radius: 50%;
  }
  .person-name {
    margin-top: 30px;
    color: var(--orange);
    font-weight: 900;
    font-size: 25px;
    letter-spacing: .2px;
  }
  .person-role {
    color: var(--grey);
    font-size: 19px;
    margin-top: 1px;
  }
  .contact-list {
    list-style: none;
    margin-top: 20px;
  }
  .contact-item {
    display: flex;
    flex-direction: column;
    align-items: center;
    margin-bottom: 9px;
  }
  .contact-icon {
    width: 17px; height: 17px;
    border-radius: 50%;
    background: var(--orange);
    display: flex; align-items: center; justify-content: center;
    margin-bottom: 4px;
  }
  .contact-icon svg { width: 11px; height: 11px; }
  .contact-text {
    color: var(--text-light);
    font-size: 17px;
    letter-spacing: .2px;
  }

  /* back */
  .back-inner {
    position: absolute;
    inset: 0;
    display: flex;
    flex-direction: column;
    align-items: center;
    padding-top: 70px;
  }
  .back-dot {
    width: 74px; height: 74px;
    border: 11px solid var(--orange);
    border-radius: 50%;
  }
  .back-wordmark {
    margin-top: 24px;
    writing-mode: vertical-rl;
    color: var(--orange);
    font-weight: 700;
    font-size: 46px;
    letter-spacing: 1px;
    line-height: 1;
  }
</style>
</head>
<body>
  <section class="card card--front" aria-label="Business card front">
    <div class="front-inner">
      <div class="brand-mark"><span class="brand-dot"></span>Velvet Pressings</div>
      <h1 class="person-name">Bram Quintel</h1>
      <p class="person-role">Founder &amp; CEO</p>
      <ul class="contact-list">
        <li class="contact-item">
          <span class="contact-icon"><svg viewBox="0 0 12 12"><path d="M3 1.5l1.6 2.2-.9 1.1c.6 1.2 1.4 2 2.5 2.5l1.1-.9 2.2 1.6-.9 1.8C5.6 9.6 2.4 6.4 1.2 2.4z" fill="#1e1e1f"/></svg></span>
          <span class="contact-text">+31620475518</span>
        </li>
        <li class="contact-item">
          <span class="contact-icon"><svg viewBox="0 0 12 12"><rect x="1.5" y="3" width="9" height="6" fill="none" stroke="#1e1e1f" stroke-width="1.2"/><path d="M1.5 3l4.5 3.5L10.5 3" fill="none" stroke="#1e1e1f" stroke-width="1.2"/></svg></span>
          <span class="contact-text">bram@velvet-pressings.example</span>
        </li>
        <li class="contact-item">
          <span class="contact-icon"><svg viewBox="0 0 12 12"><circle cx="6" cy="6" r="4.3" fill="none" stroke="#1e1e1f" stroke-width="1.1"/><path d="M1.7 6h8.6M6 1.7c-2 2.4-2 6.2 0 8.6M6 1.7c2 2.4 2 6.2 0 8.6" fill="none" stroke="#1e1e1f" stroke-width="1"/></svg></span>
          <span class="contact-text">www.velvet-pressings.example</span>
        </li>
        <li class="contact-item">
          <span class="contact-icon"></span>
          <span class="contact-text">/velvetpress</span>
        </li>
        <li class="contact-item">
          <span class="contact-icon"></span>
          <span class="contact-text">/velvetpress</span>
        </li>
        <li class="contact-item">
          <span class="contact-icon"></span>
          <span class="contact-text">/velvetpressings</span>
        </li>
      </ul>
    </div>
  </section>

  <section class="card card--back" aria-label="Business card back">
    <div class="back-inner">
      <span class="back-dot"></span>
      <p class="back-wordmark">Velvet Pressings</p>
    </div>
  </section>
</body>
</html>
```